Crestwell Renewal Business Card Design Phase 2

Professional and clean design. The design colors should flow with the logo. Two-sided card with the website on the back which is:

www.CrestwellRenewal.example.

"Specializing in Water Damage Restoration"

On the front I need the name, email, phone, and logo.

Name: Dorian Halvek
Email: Dorian@CrestwellRenewal.example
Phone: 555-318-2046 for now

I only have the Preview and Thumbnail right now but should have the source files uploaded within a day or two.

Target Market(s)

Flood victims, home owners with water damage from busted pipes etc...

Industry/Entity Type

Business

Contact Information for Business Card

Name: Dorian Halvek

Font styles to use
Serif
Sans Serif

Requirements
Must have
• Business Card Details Info

```html
<!DOCTYPE html>
<html lang="en">
<head>
<meta charset="utf-8">
<title>Crestwell Renewal Business Card</title>
<link rel="stylesheet" href="https://fonts.googleapis.com/css2?family=Anton&family=Roboto+Condensed:wght@400;700&display=swap">
<style>
  :root {
    --navy: #1f3f78;
    --navy-deep: #17315f;
    --navy-light: #2d5496;
    --green: #5cb85c;
    --white: #ffffff;
    --paper: #f4f5f7;
    --stage: #e4e5e8;
  }
  * { margin: 0; padding: 0; box-sizing: border-box; }
  html, body { width: 1200px; height: 1023px; overflow: hidden; }
  body {
    background: var(--stage);
    position: relative;
    font-family: "Roboto Condensed", Arial, sans-serif;
  }
  .card {
    position: absolute;
    left: 180px;
    width: 840px;
    height: 480px;
    overflow: hidden;
    border-radius: 4px;
    box-shadow: 0 6px 18px rgba(0,0,0,0.18);
  }
  .card--front { top: 22px; background: var(--paper); }
  .card--back {
    top: 521px;
    background: radial-gradient(ellipse at 60% 40%, var(--navy-light), var(--navy-deep) 75%);
  }
  .swoosh { position: absolute; inset: 0; width: 100%; height: 100%; }

  .wordmark {
    font-family: "Anton", Impact, sans-serif;
    text-transform: uppercase;
    line-height: 0.95;
    letter-spacing: 1px;
  }
  .card--front .wordmark {
    position: absolute;
    left: 48px;
    top: 150px;
    font-size: 66px;
    color: var(--navy);
  }

  .contact {
    position: absolute;
    right: 44px;
    top: 70px;
    width: 360px;
    text-align: right;
    color: var(--white);
  }
  .contact__name {
    font-weight: 700;
    font-size: 34px;
    color: var(--green);
    text-transform: uppercase;
    letter-spacing: 1px;
  }
  .contact__title { font-size: 20px; margin-top: 2px; margin-bottom: 70px; }
  .contact__line {
    display: flex;
    justify-content: flex-end;
    align-items: center;
    gap: 10px;
    font-size: 20px;
    margin-top: 10px;
  }
  .icon {
    width: 20px; height: 20px;
    background: var(--green);
    border-radius: 3px;
    display: inline-flex;
    align-items: center;
    justify-content: center;
  }
  .icon svg { width: 14px; height: 14px; }

  .back__content {
    position: absolute;
    inset: 0;
    display: flex;
    flex-direction: column;
    align-items: center;
    justify-content: center;
    color: var(--white);
  }
  .tagline {
    font-weight: 700;
    font-size: 17px;
    letter-spacing: 1.5px;
    text-transform: uppercase;
    margin-bottom: 10px;
  }
  .card--back .wordmark {
    font-size: 92px;
    color: var(--white);
    text-align: center;
  }
  .back__web {
    position: absolute;
    bottom: 44px;
    left: 0; right: 0;
    text-align: center;
    font-size: 24px;
    letter-spacing: 1px;
    color: var(--white);
  }
  .back__web .accent { color: var(--green); }
</style>
</head>
<body>

<section class="card card--front" aria-label="Business card front">
  <svg class="swoosh" viewBox="0 0 840 480" preserveAspectRatio="none" aria-hidden="true">
    <defs>
      <linearGradient id="navyFill" x1="0" y1="0" x2="1" y2="1">
        <stop offset="0" stop-color="#2d5496"/>
        <stop offset="1" stop-color="#1a356a"/>
      </linearGradient>
    </defs>
    <path d="M470 -5 C400 80 430 250 360 355 C310 430 220 470 110 485" fill="none" stroke="#5cb85c" stroke-width="14"/>
    <path d="M505 0 C430 70 465 250 392 360 C335 440 240 475 140 480 L840 480 L840 0 Z" fill="url(#navyFill)"/>
    <path d="M360 330 C330 410 230 455 60 470" fill="none" stroke="#1f3f78" stroke-width="8"/>
  </svg>

  <div class="wordmark">Crestwell<br>Renewal</div>

  <div class="contact">
    <div class="contact__name">Dorian Halvek</div>
    <div class="contact__title">Director</div>
    <div class="contact__line">
      <span>555-318-2046</span>
      <span class="icon"><svg viewBox="0 0 24 24"><path fill="#fff" d="M6.6 10.8a15 15 0 0 0 6.6 6.6l2.2-2.2c.3-.3.7-.4 1-.2 1.1.4 2.3.6 3.6.6.6 0 1 .4 1 1V20c0 .6-.4 1-1 1A17 17 0 0 1 3 4c0-.6.4-1 1-1h3.5c.6 0 1 .4 1 1 0 1.3.2 2.5.6 3.6.1.3 0 .7-.2 1z"/></svg></span>
    </div>
    <div class="contact__line">
      <span>Dorian@CrestwellRenewal.example</span>
      <span class="icon"><svg viewBox="0 0 24 24"><path fill="#fff" d="M3 5h18v14H3z"/><path fill="none" stroke="#5cb85c" stroke-width="2" d="M3 6l9 7 9-7"/></svg></span>
    </div>
    <div class="contact__line">
      <span>www.CrestwellRenewal.example</span>
      <span class="icon"><svg viewBox="0 0 24 24"><circle cx="12" cy="12" r="9" fill="none" stroke="#fff" stroke-width="2"/><path d="M3 12h18M12 3c3 3 3 15 0 18M12 3c-3 3-3 15 0 18" fill="none" stroke="#fff" stroke-width="1.6"/></svg></span>
    </div>
  </div>
</section>

<section class="card card--back" aria-label="Business card back">
  <div class="back__content">
    <div class="tagline">Specializing in Water Damage Restoration</div>
    <div class="wordmark">Crestwell<br>Renewal</div>
  </div>
  <div class="back__web">www.Crestwell<span class="accent">Renewal</span>.example</div>
</section>

</body>
</html>
```